I work in creative/artistic projects across different mediums.
It needs to communicate creativity, style, sexy, uniqueness, individuality and sophistication.
It should not look corporate.
Colours I like are black silver gold deep purple, chocolate, orchid.
It doesn't have to make use of all these colours.
I do not like bright primary colors.
Updates

Project Deadline Extended
Reason: Still in the communication process and to allow the person enough time to finish the design. Though i should know in the next day or two. Thank you.

Target Market(s)

creatives and companies wanting to inject creativity into thier business.

Industry/Entity Type

Work

Contact Information for Business Card

Marcus Tellwick
0418592036
marcus@marcustellwick.com

quietgoldenhour.com.au

Requirements
Should not have
• Anything corporate OR OLD FASHIONED

```html
<!DOCTYPE html>
<html lang="en">
<head>
<meta charset="utf-8">
<title>Marcus Tellwick — Business Card</title>
<link rel="stylesheet" href="https://fonts.googleapis.com/css2?family=Oswald:wght@300;400&display=swap">
<style>
  :root {
    --backdrop: #1c1c1e;
    --card-deep: #3a3296;
    --card-mid: #4b43b4;
    --card-light: #5b55c4;
    --gold: #ecc64c;
    --gold-soft: #d9b13d;
  }
  * { box-sizing: border-box; margin: 0; padding: 0; }
  html, body {
    width: 1200px;
    height: 700px;
    overflow: hidden;
    background: var(--backdrop);
  }
  .canvas {
    width: 1200px;
    height: 700px;
    display: flex;
    align-items: center;
    justify-content: center;
  }
  .business-card {
    position: relative;
    width: 900px;
    height: 514px;
    overflow: hidden;
    border-radius: 4px;
  }
  .leaf-pattern-area {
    position: absolute;
    inset: 0;
    background:
      radial-gradient(ellipse at 55% 40%, var(--card-light) 0%, var(--card-mid) 45%, var(--card-deep) 100%);
  }
  .card-content {
    position: relative;
    height: 100%;
    display: flex;
    flex-direction: column;
    align-items: center;
    padding-top: 118px;
    font-family: "Oswald", "Arial Narrow", sans-serif;
    color: var(--gold);
  }
  .name-rule { display: block; }
  .name {
    font-weight: 300;
    font-size: 54px;
    letter-spacing: 3px;
    line-height: 1;
    text-transform: uppercase;
    margin: 14px 0 12px;
  }
  .contact-list {
    list-style: none;
    text-align: center;
    margin-top: 30px;
    font-weight: 300;
    font-size: 25px;
    letter-spacing: 1.5px;
    line-height: 1.35;
  }
  .contact-list .phone { margin-bottom: 10px; }
  .closing-dash {
    width: 36px;
    height: 3px;
    background: var(--gold-soft);
    margin-top: 26px;
  }
</style>
</head>
<body>
  <main class="canvas">
    <section class="business-card">
      <div class="leaf-pattern-area" role="img" aria-label="Deep violet background covered with large overlapping outlined leaves"></div>
      <div class="card-content">
        <svg class="name-rule name-rule--top" width="250" height="8" viewBox="0 0 250 8" aria-hidden="true">
          <line x1="0" y1="4" x2="250" y2="4" stroke="var(--gold)" stroke-width="1.5"/>
          <line x1="95" y1="4" x2="155" y2="4" stroke="var(--gold)" stroke-width="4" stroke-linecap="round"/>
        </svg>
        <h1 class="name">Marcus Tellwick</h1>
        <svg class="name-rule name-rule--bottom" width="180" height="8" viewBox="0 0 180 8" aria-hidden="true">
          <line x1="0" y1="4" x2="180" y2="4" stroke="var(--gold)" stroke-width="1.5"/>
          <line x1="60" y1="4" x2="120" y2="4" stroke="var(--gold)" stroke-width="4" stroke-linecap="round"/>
        </svg>
        <ul class="contact-list">
          <li class="phone">0418592036</li>
          <li class="email">marcus@marcustellwick.com</li>
          <li class="website">www.quietgoldenhour.com.au</li>
        </ul>
        <div class="closing-dash" aria-hidden="true"></div>
      </div>
    </section>
  </main>
</body>
</html>
```